Innovative Healthcare Technology Company needs a Business Card Design

We are in need of an innovative business card design for a new healthcare software company called "Lumenwise Data Partners". We develop software that creates medical assessment applications and mobile e-learning prevention services to reduce risk behaviors in adolescent and young adults. Our initial product, the "KESTREL App", conducts a tailored sexual risk assessment and provides a doctor with an insightful patient report to improve sexual risk counseling and ultimately reduce unintended pregnancy, STDs, etc.

We would like the design to incorporate our logo and branding colors (attached) in an innovative and creative manner. The final design should communicate professionalism and healthcare innovation. Our tag line is "Clarity leads to better care" (doesn't necessarily need to be included) and our target audience is doctors, medical directors, and medical business administrators. Please visit our website for additional info ourbrightmarq.com. Be creative and we look forward to seeing your designs!

Target Market(s)

healthcare - doctors, medical directors and medical business administrators

Industry/Entity Type

Healthcare

Contact Information for Business Card

We would like the design to incorporate our logo and branding colors (attached) in an innovative and creative manner. The final design should communicate professionalism and healthcare innovation. Our tag line is "Clarity leads to better care" (doesn't necessarily need to be included)

Font styles to use
Other font styles liked:
• quicksand

Requirements
Must have
• our logo and brand colors
• Name, (Mara Feldhovenik, PhD)
• Email (drmara@ourbrightmarq.com)
• phone (555.283.9170)
• Website (ourbrightmarq.com)
Should not have
• cartoon look

```html
<!DOCTYPE html>
<html lang="en">
<head>
<meta charset="utf-8">
<title>Lumenwise Data Partners — Business Card</title>
<link rel="stylesheet" href="https://fonts.googleapis.com/css2?family=Quicksand:wght@400;500;700&display=swap">
<style>
  :root {
    --brand-blue: #0b4a8b;
    --brand-green: #6a9a86;
    --card-white: #f2f2f2;
    --ink-gray: #4a4a4a;
    --rule-gray: #9a9a9a;
    --backdrop: #3b3b3b;
  }
  * { margin: 0; padding: 0; box-sizing: border-box; }
  html, body { width: 1200px; height: 750px; overflow: hidden; }
  body {
    background: var(--backdrop);
    font-family: "Quicksand", sans-serif;
    position: relative;
  }
  .card {
    position: absolute;
    top: 228px;
    width: 462px;
    height: 263px;
    border-radius: 12px;
    padding: 9px;
  }
  .card-front { left: 124px; background: var(--brand-blue); }
  .card-back  { left: 618px; background: var(--card-white); }
  .card-face {
    position: relative;
    width: 100%;
    height: 100%;
    border-radius: 12px;
  }
  .card-front .card-face { background: var(--card-white); }
  .card-back .card-face { background: var(--brand-blue); }

  .brand {
    position: absolute;
    top: 44px;
    right: 20px;
    display: flex;
    align-items: center;
    gap: 9px;
  }
  .brand-square {
    width: 14px;
    height: 14px;
    background: var(--brand-blue);
  }
  .brand-name {
    font-size: 21px;
    font-weight: 500;
    color: var(--brand-blue);
    letter-spacing: 0.3px;
    white-space: nowrap;
  }

  .person {
    position: absolute;
    left: 22px;
    right: 18px;
    top: 128px;
  }
  .person-name {
    font-size: 16px;
    font-weight: 700;
    color: var(--brand-blue);
    letter-spacing: 0.3px;
  }
  .person-name .credential { font-size: 11.5px; }
  .person-title {
    display: flex;
    align-items: flex-end;
    margin-top: 1px;
    font-size: 12.5px;
    color: var(--brand-green);
    letter-spacing: 0.6px;
  }
  .person-title .rule {
    flex: 1;
    height: 1px;
    background: var(--rule-gray);
    margin-bottom: 3px;
  }

  .contacts {
    position: absolute;
    left: 22px;
    top: 182px;
    list-style: none;
  }
  .contacts li {
    display: flex;
    align-items: center;
    gap: 6px;
    height: 17.5px;
    font-size: 11.5px;
    color: var(--ink-gray);
    letter-spacing: 0.5px;
  }
  .contacts svg { width: 12px; height: 12px; fill: var(--brand-blue); }

  .back-brand {
    position: absolute;
    left: 0; right: 0;
    top: 96px;
    display: flex;
    justify-content: center;
    align-items: center;
    gap: 10px;
  }
  .back-brand .brand-square { background: var(--card-white); width: 16px; height: 16px; }
  .back-brand .brand-name { color: var(--card-white); font-size: 24px; }
  .tagline {
    position: absolute;
    left: 0; right: 0;
    top: 213px;
    text-align: center;
    font-size: 14px;
    font-style: italic;
    color: var(--card-white);
    letter-spacing: 0.3px;
  }
</style>
</head>
<body>
  <section class="card card-front">
    <div class="card-face">
      <div class="brand">
        <span class="brand-square"></span>
        <span class="brand-name">Lumenwise Data Partners</span>
      </div>

      <div class="person">
        <p class="person-name">Mara Feldhovenik, <span class="credential">PhD</span></p>
        <p class="person-title"><span>CEO/Founder</span><span class="rule"></span></p>
      </div>

      <ul class="contacts">
        <li>
          <svg viewBox="0 0 24 24" aria-hidden="true"><path d="M6.6 10.8a15.1 15.1 0 0 0 6.6 6.6l2.2-2.2a1 1 0 0 1 1-.25 11.4 11.4 0 0 0 3.6.57 1 1 0 0 1 1 1V20a1 1 0 0 1-1 1A17 17 0 0 1 3 4a1 1 0 0 1 1-1h3.5a1 1 0 0 1 1 1c0 1.25.2 2.450.57 3.57a1 1 0 0 1-.25 1z"/></svg>
          555.283.9170
        </li>
        <li>
          <svg viewBox="0 0 24 24" aria-hidden="true"><path d="M2 5h20v14H2z M4 7v.3l8 5.2 8-5.2V7z" fill-rule="evenodd"/></svg>
          drmara@ourbrightmarq.com
        </li>
        <li>
          <svg viewBox="0 0 24 24" aria-hidden="true"><path d="M12 2a10 10 0 1 0 0 20 10 10 0 0 0 0-20zm-1 17.9A8 8 0 0 1 4.1 11H7c.1 3.3 1.6 6.4 4 8.9zM7 9H4.3A8 8 0 0 1 11 4.1 12.8 12.8 0 0 0 7 9zm6 10.9c2.4-2.5 3.9-5.6 4-8.9h2.9a8 8 0 0 1-6.9 8.9zM17 9a12.8 12.8 0 0 0-4-4.9A8 8 0 0 1 19.7 9z"/></svg>
          www.ourbrightmarq.com
        </li>
      </ul>
    </div>
  </section>

  <section class="card card-back">
    <div class="card-face">
      <div class="back-brand">
        <span class="brand-square"></span>
        <span class="brand-name">Lumenwise Data Partners</span>
      </div>
      <p class="tagline">Clarity leads to better care</p>
    </div>
  </section>
</body>
</html>
```